Business Card Design

We are starting up a new Family run Business mainly offering a Free House Clearance service. We also offer the following chargeable services which include a Removals Service, Delivery and Collection of Items sold or purchased on Bidloft, Swapwren etc, including Motorcycles, Piano's, Furniture, Electrical appliances.
As there are a few Companies offering similar services we need to stand out and show what we do at a glance while appearing Professional and approachable
Updates

TidyNests

i  am liking some of the colours and designs so far but would like to see a few of our services listed as 1 or 2 have already done if this is possible and maybe some emphasis on the FREE House Clearance. thank you 
best regards
derek

Target Market(s)

Commercial and Domestic Tenants and Landlords aswell as Families looking for a friendly sympathetic clearance service after bereavement

Industry/Entity Type

Business

Contact Information for Business Card

TidyNests,
HouseClearance and Removals,
Marlow Dene
LM47 2QT
Tel: 07815239604
Email: enquiries@tidynests-example.info

```html
<!DOCTYPE html>
<html lang="en">
<head>
<meta charset="utf-8">
<title>TidyNests Business Card</title>
<link rel="stylesheet" href="https://fonts.googleapis.com/css2?family=Gelasio:wght@400;700&display=swap">
<style>
  :root {
    --page-bg: #ffffff;
    --card-blue: #55b0d8;
    --brand-tint: #a9d8ee;
    --text-soft: #c4e6f5;
    --text-white: #ffffff;
  }
  * { margin: 0; padding: 0; box-sizing: border-box; }
  html, body {
    width: 1200px; height: 1000px; overflow: hidden;
    background: var(--page-bg);
    font-family: "Gelasio", Georgia, serif;
  }
  .canvas { position: relative; width: 1200px; height: 1000px; }
  .card {
    position: absolute; left: 346px; width: 519px; height: 342px;
    background: var(--card-blue);
  }
  .card--front { top: 155px; }
  .card--back { top: 519px; }

  /* Front */
  .brand-lockup {
    position: absolute; left: 0; right: 0; top: 262px; text-align: center;
    color: var(--brand-tint);
  }
  .card--front .brand-lockup { top: 95px; }
  .brand-mark {
    display: block; width: 44px; height: 44px; margin: 0 auto 22px;
    background: var(--brand-tint); opacity: 0.7;
  }
  .brand-name {
    font-size: 30px; font-weight: 400; letter-spacing: 1px; line-height: 1;
  }
  .brand-tagline {
    margin-top: 12px; font-size: 11px; letter-spacing: 1px; line-height: 1;
  }
  .contact-row {
    position: absolute; left: 23px; right: 23px; top: 305px;
    display: flex; justify-content: space-between;
    font-size: 12.5px; color: var(--text-soft); letter-spacing: 0.3px;
  }
  .contact-row b { color: var(--text-white); font-weight: 700; }

  /* Back */
  .services-title {
    position: absolute; left: 46px; top: 76px;
    font-size: 20px; color: var(--text-white); font-weight: 400; letter-spacing: 0.3px;
  }
  .services-rule {
    position: absolute; left: 43px; top: 110px; width: 181px; height: 5px;
    background: var(--text-white);
  }
  .services-list {
    position: absolute; left: 46px; top: 124px; width: 420px;
    font-size: 16px; line-height: 20px; color: var(--text-soft); letter-spacing: 0.4px;
  }
  .services-list strong { color: var(--text-white); font-weight: 700; }
  .brand-lockup--small {
    left: auto; right: 24px; top: 288px; text-align: left;
  }
  .brand-lockup--small .brand-name { font-size: 15px; letter-spacing: 0.5px; }
  .brand-lockup--small .brand-tagline { margin-top: 4px; font-size: 6px; letter-spacing: 0.4px; }
</style>
</head>
<body>
<div class="canvas">
  <section class="card card--front">
    <div class="brand-lockup">
      <span class="brand-mark"></span>
      <div class="brand-name">TIDYNESTS</div>
      <div class="brand-tagline">HOUSE CLEARANCE &amp; REMOVALS</div>
    </div>
    <div class="contact-row">
      <span>Marlow Dene LM47 2QT</span>
      <span><b>T</b> 07815239604</span>
      <span><b>E</b> enquiries@tidynests-example.info</span>
    </div>
  </section>

  <section class="card card--back">
    <h2 class="services-title">Services include</h2>
    <div class="services-rule"></div>
    <p class="services-list">
      <strong>Free</strong> House Clearance<br>
      and <strong>Chargeable</strong> Removals Service, Delivery and<br>
      Collection of Items sold or purchased on<br>
      Bidloft, Swapwren etc.
    </p>
    <div class="brand-lockup brand-lockup--small">
      <div class="brand-name">TIDYNESTS</div>
      <div class="brand-tagline">HOUSE CLEARANCE &amp; REMOVALS</div>
    </div>
  </section>
</div>
</body>
</html>
```